Jewelry Back Card Graphic Design

I am looking for a graphic design to print out and put in the back of the jewelry box for my long-distance jewelry. I attached an example that I am now using for the "still harbor jewelry" so you can see what it's used for.

But this card needs to relate to people who are in a long-distance relationship or friendship, so it needs to resonate with them when they see it on the website and open the box if they receive the jewelry as a gift.

I attached a rough idea that I sketched myself, but you can be creative and create anything else if you have a better idea.

It needs to be square.

Looking forward to the results!

```html
<!DOCTYPE html>
<html lang="en">
<head>
<meta charset="utf-8">
<title>Long-Distance Keepsake Card</title>
<link rel="stylesheet" href="https://fonts.googleapis.com/css2?family=Yellowtail&display=swap">
<style>
  :root {
    --page: #ffffff;
    --ink: #ffffff;
    --ink-shadow: #111111;
    --sky-top: #7f72d4;
    --sky-mid: #aaa4f2;
    --haze: #e3b2cf;
    --glow: #f3966f;
    --sun: #ffe55a;
    --horizon: #cf2414;
    --sea: #f19a72;
    --sand: #c65565;
    --sand-deep: #7f2f45;
  }
  html, body {
    margin: 0;
    padding: 0;
    width: 1200px;
    height: 1200px;
    overflow: hidden;
    background: var(--page);
  }
  .canvas {
    position: relative;
    width: 1200px;
    height: 1200px;
    background: var(--page);
  }
  .card {
    position: absolute;
    left: 218px;
    top: 218px;
    width: 768px;
    height: 768px;
  }
  .card__scene {
    position: absolute;
    inset: 0;
    width: 100%;
    height: 100%;
    display: block;
  }
  .card__quote {
    position: absolute;
    left: 0;
    right: 0;
    top: 166px;
    margin: 0;
    text-align: center;
    font-family: "Yellowtail", cursive;
    font-weight: 400;
    font-size: 66px;
    line-height: 132px;
    color: var(--ink);
    text-shadow: 4px 4px 0 var(--ink-shadow);
    letter-spacing: 0.5px;
  }
  .card__quote-line { display: block; }
  .card__quote-line--first { margin-left: 60px; }
</style>
</head>
<body>
  <main class="canvas">
    <section class="card">
      <svg class="card__scene" viewBox="0 0 768 768" role="img" aria-label="Blurred long-exposure photograph of a sunset over the sea and a sandy beach with footprints">
        <defs>
          <linearGradient id="sunsetFill" x1="0" y1="0" x2="0" y2="1">
            <stop offset="0" stop-color="var(--sky-top)"/>
            <stop offset="0.22" stop-color="var(--sky-mid)"/>
            <stop offset="0.42" stop-color="var(--haze)"/>
            <stop offset="0.52" stop-color="var(--glow)"/>
            <stop offset="0.57" stop-color="var(--sun)"/>
            <stop offset="0.6" stop-color="#fff4c0"/>
            <stop offset="0.615" stop-color="var(--horizon)"/>
            <stop offset="0.64" stop-color="var(--sea)"/>
            <stop offset="0.72" stop-color="#e57c7e"/>
            <stop offset="0.8" stop-color="var(--sand)"/>
            <stop offset="1" stop-color="var(--sand-deep)"/>
          </linearGradient>
        </defs>
        <rect width="768" height="768" fill="url(#sunsetFill)"/>
      </svg>
      <p class="card__quote">
        <span class="card__quote-line card__quote-line--first">No matter the distance,</span>
        <span class="card__quote-line">you'll always</span>
        <span class="card__quote-line">be in my heart</span>
      </p>
    </section>
  </main>
</body>
</html>
```